Stationery Design Project

I need a design that is simple, clean and modern, in square style, bold font.
The majority of the design needs to be White and Black with a splash of Red colour.
I would like a design for business cards and letter heads with the following information.
Name, Title, Phone, Fax, Email, Website and company ABN number

Target Market(s)

25 to 65 years old real estate clients

Industry/Entity Type

Business

Requirements
Must have
• All designs must incorporate Company Logo, Name, Title, Phone, Fax, Email, Website and company ABN number

```html
<!DOCTYPE html>
<html lang="en">
<head>
<meta charset="utf-8">
<title>Northgate Real Estate – Business Card</title>
<link href="https://fonts.googleapis.com/css2?family=Lato:wght@400;700&display=swap" rel="stylesheet">
<style>
  :root {
    --paper: #ffffff;
    --ink: #2b2b2b;
    --ink-soft: #3a3a3a;
    --charcoal: #2f2f2f;
    --accent: #e3202b;
    --backdrop: #e6e8ea;
  }
  * { box-sizing: border-box; margin: 0; padding: 0; }
  html, body {
    width: 1200px; height: 960px; overflow: hidden;
    background: var(--backdrop);
    font-family: "Lato", Arial, sans-serif;
    color: var(--ink);
  }
  .sheet {
    width: 1200px; height: 960px;
    display: flex; flex-direction: column;
    align-items: center; justify-content: center; gap: 40px;
  }
  .card {
    width: 700px; height: 400px; position: relative;
    box-shadow: 0 8px 24px rgba(0,0,0,.18);
  }
  .card--front { background: var(--paper); }
  .card--back { background: var(--charcoal); display: flex; align-items: center; justify-content: center; }

  .holder { position: absolute; left: 44px; top: 70px; }
  .holder__name {
    font-size: 32px; font-weight: 400; letter-spacing: .5px; color: var(--ink);
    padding-bottom: 4px; border-bottom: 2px solid var(--accent); display: inline-block;
  }
  .holder__title { font-size: 19px; margin-top: 6px; color: var(--ink-soft); }

  .contacts { position: absolute; left: 44px; top: 200px; list-style: none; }
  .contacts li { display: flex; align-items: center; gap: 14px; font-size: 19px; line-height: 30px; color: var(--ink-soft); }
  .contacts svg { width: 20px; height: 20px; flex: none; }

  .legal { position: absolute; left: 44px; bottom: 40px; font-size: 19px; line-height: 28px; }
  .legal__web { color: var(--accent); font-weight: 700; }

  .brand { position: absolute; right: 40px; top: 190px; display: flex; align-items: center; gap: 12px; }
  .brand__mark { width: 16px; height: 16px; background: var(--accent); }
  .brand__name { font-size: 30px; font-weight: 700; letter-spacing: 2px; color: var(--ink); }
  .brand__sub { position: absolute; right: 40px; top: 240px; font-size: 15px; letter-spacing: 9px; color: var(--ink); }

  .back-brand { display: flex; align-items: center; gap: 18px; }
  .back-brand__mark { width: 26px; height: 26px; background: var(--accent); }
  .back-brand__name { font-size: 54px; font-weight: 700; letter-spacing: 4px; color: var(--paper); }
</style>
</head>
<body>
<main class="sheet">
  <section class="card card--front">
    <div class="holder">
      <h1 class="holder__name">HELENA MARSH</h1>
      <p class="holder__title">Operation Manager</p>
    </div>

    <ul class="contacts">
      <li>
        <svg viewBox="0 0 20 20" aria-hidden="true"><rect x="3" y="2" width="14" height="16" rx="2" fill="none" stroke="var(--accent)" stroke-width="2"/><rect x="6" y="5" width="8" height="3" fill="var(--accent)"/><rect x="6" y="11" width="8" height="4" fill="var(--accent)"/></svg>
        (555) 01 204 18 37
      </li>
      <li>
        <svg viewBox="0 0 20 20" aria-hidden="true"><rect x="5" y="2" width="10" height="6" fill="none" stroke="var(--accent)" stroke-width="2"/><rect x="2" y="8" width="16" height="7" rx="1" fill="var(--accent)"/><rect x="5" y="13" width="10" height="5" fill="var(--paper)" stroke="var(--accent)" stroke-width="2"/></svg>
        (555) 01 204 18 38
      </li>
      <li>
        <svg viewBox="0 0 20 20" aria-hidden="true"><rect x="2" y="4" width="16" height="12" fill="none" stroke="var(--accent)" stroke-width="2"/><path d="M2 4l8 7 8-7" fill="none" stroke="var(--accent)" stroke-width="2"/></svg>
        name@northgate-realty.com
      </li>
    </ul>

    <div class="legal">
      <p>ABN 987654321</p>
      <p class="legal__web">www.northgate-realty.com</p>
    </div>

    <div class="brand">
      <span class="brand__mark"></span>
      <span class="brand__name">NORTHGATE</span>
    </div>
    <p class="brand__sub">REAL ESTATE</p>
  </section>

  <section class="card card--back">
    <div class="back-brand">
      <span class="back-brand__mark"></span>
      <span class="back-brand__name">NORTHGATE</span>
    </div>
  </section>
</main>
</body>
</html>
```